Hello,
Just to let you know this is urgent, please.

We are needing an A5 Advertisement for the back page of a calendar booklet. We need it to look sharp and elegant.
To keep it simple we would like to use logo as the graphic.
Attached below is the copy and a dropbox link for a selection of logos and the brand guidelines.
I look forward to receiving your designs.
Many thanks
Marjorie

```html
<!DOCTYPE html>
<html lang="en">
<head>
<meta charset="utf-8">
<title>Kestrel Ridge Polo Club – Season Advertisement</title>
<link rel="stylesheet" href="https://fonts.googleapis.com/css2?family=Nunito:wght@700;800;900&family=Montserrat:wght@500;600&family=Lato:wght@400&display=swap">
<style>
  :root {
    --ink: #1c1c1c;
    --ink-soft: #3a3a3a;
    --paper: #ffffff;
    --band: #1b1b1b;
    --rule: #4a4a4a;
    --silver-a: #f3f3f3;
    --silver-b: #9a9a9a;
    --gold-a: #e0b300;
    --gold-b: #7a5d08;
    --ribbon-a: #5c5c5c;
    --ribbon-b: #2a2a2a;
  }
  * { margin: 0; padding: 0; box-sizing: border-box; }
  html, body { width: 917px; height: 1200px; overflow: hidden; background: var(--paper); }
  .advert {
    position: relative; width: 917px; height: 1200px; overflow: hidden;
    background: var(--paper); color: var(--ink);
    font-family: "Montserrat", Arial, sans-serif;
  }
  .backdrop {
    position: absolute; inset: 0 0 244px 0;
    background:
      radial-gradient(ellipse at 20% 30%, rgba(170,170,170,.45), transparent 60%),
      radial-gradient(ellipse at 85% 60%, rgba(200,200,200,.35), transparent 55%),
      linear-gradient(160deg, #e6e6e6 0%, #f7f7f7 45%, #ececec 100%);
  }
  .event { position: absolute; left: 0; width: 917px; }
  .event__frame {
    position: absolute; left: 103px; width: 712px;
    border: 1.5px solid var(--rule);
  }
  .event__title {
    position: absolute; height: 72px; width: 512px; left: 203px;
    clip-path: polygon(0 0, 96% 0, 100% 100%, 3% 100%);
    display: flex; align-items: center; justify-content: center;
    font-family: "Nunito", Arial, sans-serif; font-weight: 900;
    font-size: 36px; letter-spacing: .5px;
  }
  .event--silver .event__title { background: linear-gradient(90deg, var(--silver-b), var(--silver-a) 30%, #dcdcdc 70%, var(--silver-b)); color: var(--ink); }
  .event--gold .event__title { background: linear-gradient(90deg, var(--gold-b), var(--gold-a) 45%, var(--gold-b)); color: #fff; }
  .event__line {
    position: absolute; left: 0; width: 917px; text-align: center;
    font-weight: 600; font-size: 28px; color: var(--ink-soft); letter-spacing: -.5px;
  }
  .event__line sup { font-size: 17px; vertical-align: -2px; }

  .club-mark {
    position: absolute; left: 0; width: 917px; top: 620px; text-align: center;
  }
  .club-mark__dot {
    display: block; width: 150px; height: 150px; margin: 0 auto 52px;
    border-radius: 50%; background: var(--ink-soft);
  }
  .club-mark__name {
    font-family: "Lato", Arial, sans-serif; font-weight: 400;
    font-size: 29px; color: var(--ink); letter-spacing: -.3px;
  }

  .contact-band { position: absolute; left: 0; top: 956px; width: 917px; height: 168px; background: var(--band); }
  .membership { position: absolute; left: 102px; top: 902px; width: 712px; height: 98px; }
  .membership__text {
    position: absolute; inset: 0; display: flex; flex-direction: column;
    align-items: center; justify-content: center; color: #fff;
    font-family: "Nunito", Arial, sans-serif; font-weight: 800; font-size: 26px; line-height: 34px;
    letter-spacing: .4px;
  }
  .contact-band__main {
    position: absolute; top: 1024px; left: 0; width: 917px; text-align: center; color: #fff;
    font-family: "Nunito", Arial, sans-serif; font-weight: 800; font-size: 33px; letter-spacing: .6px;
    display: flex; justify-content: center; align-items: center; gap: 10px;
  }
  .contact-band__address {
    position: absolute; top: 1076px; left: 0; width: 917px; color: #fff;
    font-family: "Nunito", Arial, sans-serif; font-weight: 700; font-size: 21px;
    display: flex; justify-content: center; align-items: center; gap: 8px;
  }
  .footer {
    position: absolute; top: 1124px; left: 0; width: 917px; height: 76px;
    display: flex; align-items: center; justify-content: center;
    font-family: "Nunito", Arial, sans-serif; font-weight: 700; font-size: 25px; color: var(--ink);
  }
  .footer__item { display: flex; align-items: center; gap: 12px; }
  .footer__divider { width: 1.5px; height: 40px; background: #555; margin: 0 30px; }
</style>
</head>
<body>
<main class="advert">
  <div class="backdrop" role="img" aria-label="Soft grey background of faded diamond tiles and halftone dots"></div>

  <section class="event event--silver">
    <div class="event__frame" style="top:146px;height:150px;"></div>
    <h2 class="event__title" style="top:111px;">KESTREL SILVER CUP</h2>
    <p class="event__line" style="top:198px;">APRIL 11<sup>th</sup>, 13<sup>th</sup> AND 14<sup>th</sup> 2019</p>
    <p class="event__line" style="top:240px;">12, 6 AND 2 GOAL AND SUB ZERO</p>
  </section>

  <section class="event event--gold">
    <div class="event__frame" style="top:403px;height:149px;"></div>
    <h2 class="event__title" style="top:367px;">KESTREL GOLD CUP</h2>
    <p class="event__line" style="top:456px;">OCTOBER 16<sup>th</sup>, 17<sup>th</sup>, 19<sup>th</sup> AND 20TH 2019</p>
    <p class="event__line" style="top:498px;">12, 6 AND 2 GOAL AND SUB ZERO</p>
  </section>

  <div class="club-mark">
    <span class="club-mark__dot"></span>
    <p class="club-mark__name">KESTREL RIDGE POLO CLUB</p>
  </div>

  <div class="contact-band"></div>

  <div class="membership">
    <svg width="712" height="98" viewBox="0 0 712 98" aria-hidden="true">
      <defs>
        <linearGradient id="ribbonFill" x1="0" y1="0" x2="0" y2="1">
          <stop offset="0" stop-color="var(--ribbon-a)"/>
          <stop offset="1" stop-color="var(--ribbon-b)"/>
        </linearGradient>
      </defs>
      <path d="M36 3 H700 Q709 3 707 12 L688 86 Q686 95 676 95 H12 Q3 95 5 86 L24 12 Q26 3 36 3 Z"
            fill="url(#ribbonFill)" stroke="#9a9a9a" stroke-width="1.5"/>
    </svg>
    <div class="membership__text"><span>PLAYING AND SOCIAL MEMBERSHIPS</span><span>NOW AVAILABLE</span></div>
  </div>

  <p class="contact-band__main">
    <span>KESTREL RIDGE POLO CLUB</span>
    <svg width="28" height="28" viewBox="0 0 24 24" aria-hidden="true"><circle cx="12" cy="12" r="10.5" fill="none" stroke="#fff" stroke-width="1.8"/><path d="M8.6 6.8l1.8-.4 1 2.6-1.2 1c.6 1.3 1.5 2.3 2.8 2.9l1-1.2 2.6 1-.4 1.8c-3.9.3-7.9-3.7-7.6-7.7z" fill="#fff"/></svg>
    <span>(02) 4511 0270</span>
  </p>
  <p class="contact-band__address">
    <svg width="16" height="20" viewBox="0 0 16 20" aria-hidden="true"><circle cx="8" cy="6.5" r="4.5" fill="none" stroke="#fff" stroke-width="1.6"/><path d="M8 11v7M4 18h8" stroke="#fff" stroke-width="1.6"/></svg>
    <span>27 Wattle Creek Road Richmond, NSW</span>
  </p>

  <footer class="footer">
    <span class="footer__item">
      <svg width="26" height="18" viewBox="0 0 26 18" aria-hidden="true"><rect x="1" y="1" width="24" height="16" fill="none" stroke="#222" stroke-width="1.6"/><path d="M1 1l12 9 12-9M1 17l9-7M25 17l-9-7" fill="none" stroke="#222" stroke-width="1.6"/></svg>
      admin@kestrelpolo.com
    </span>
    <span class="footer__divider"></span>
    <span class="footer__item">
      <svg width="22" height="22" viewBox="0 0 22 22" aria-hidden="true"><g fill="none" stroke="#222" stroke-width="1.6"><circle cx="11" cy="11" r="9.5"/><ellipse cx="11" cy="11" rx="4.2" ry="9.5"/><path d="M1.5 11h19M3 6h16M3 16h16"/></g></svg>
      www.kestrelpolo.com
    </span>
  </footer>
</main>
</body>
</html>
```